Business card with logo for a family psychologist

I need a business card for my private practice in the urban Chicago area as a psychologist. I see families and individuals who are going through difficult times - divorce, separation, illness, or trauma. I want to project hopefulness, competence, and caring.

Target Market(s)

Adults, other professionals - such as physicans and lawyers

Industry/Entity Type

Health Care

Contact Information for Business Card

Front should have my name and credentials; back should have location information including my email, phone

Font styles to use
Serif
Decorative
Script

Requirements
Must have
• Unique logo
Should not have
• No pictures or icons of people; no black

```html
<!DOCTYPE html>
<html lang="en">
<head>
<meta charset="utf-8">
<title>Dana Whitfield, Ph.D. — Business Card</title>
<link href="https://fonts.googleapis.com/css2?family=Open+Sans:wght@400;700&display=swap" rel="stylesheet">
<style>
  :root {
    --navy: #2a3a8c;
    --royal: #3a4fb0;
    --deep: #24337e;
    --paper: #ffffff;
    --backdrop: #d4d4d6;
    --ink-grey: #5f6068;
    --rule: #9a9aa2;
    --tab: #4a5fc8;
  }
  * { box-sizing: border-box; margin: 0; padding: 0; }
  html, body {
    width: 1200px; height: 800px; overflow: hidden;
    background: var(--backdrop);
    font-family: "Open Sans", Arial, sans-serif;
  }
  .stage {
    position: relative; width: 1200px; height: 800px;
    display: flex; align-items: center; justify-content: center; gap: 60px;
  }
  .card {
    position: relative; width: 525px; height: 300px; overflow: hidden;
    box-shadow: 0 2px 6px rgba(0,0,0,.12);
  }
  .card--front {
    background: linear-gradient(115deg, var(--deep) 0%, var(--navy) 35%, var(--royal) 55%, var(--navy) 75%, var(--deep) 100%);
    color: var(--paper);
  }
  .card--back { background: var(--paper); color: var(--navy); }

  .tab { position: absolute; width: 26px; height: 12px; }
  .tab--top { top: 0; }
  .tab--bottom { bottom: 0; }

  .identity {
    position: absolute; display: flex; flex-direction: column; align-items: center;
  }
  .identity__mark {
    width: 46px; height: 46px; border-radius: 50%;
    border: 2px solid currentColor; margin-bottom: 10px;
  }
  .identity__name { font-weight: 700; font-size: 30px; letter-spacing: .3px; line-height: 1.1; }
  .identity__title { font-weight: 400; font-size: 15px; margin-top: 4px; }

  .card--front .identity { left: 0; right: 0; top: 72px; }

  .card--back .identity { left: 40px; top: 150px; }
  .card--back .identity__name { font-size: 26px; }
  .card--back .identity__title { font-size: 13px; }

  .contact {
    position: absolute; left: 268px; top: 34px;
    padding-left: 22px; border-left: 1px solid var(--rule);
    color: var(--ink-grey); font-size: 12px; line-height: 1.6;
  }
  .contact__row { display: flex; align-items: flex-start; gap: 8px; white-space: nowrap; }
  .contact__icon { width: 11px; height: 11px; margin-top: 4px; flex: none; }
  .contact__address { display: flex; flex-direction: column; }
</style>
</head>
<body>
<main class="stage">

  <section class="card card--front" aria-label="Card front">
    <svg class="tab tab--top" style="left:300px" viewBox="0 0 26 12"><polygon points="0,0 26,0 20,12 6,12" fill="var(--tab)" opacity=".7"/></svg>
    <svg class="tab tab--bottom" style="left:120px" viewBox="0 0 26 12"><polygon points="6,0 20,0 26,12 0,12" fill="var(--tab)" opacity=".7"/></svg>
    <div class="identity">
      <span class="identity__mark"></span>
      <h1 class="identity__name">Dana Whitfield, Ph.D.</h1>
      <p class="identity__title">Licensed Clinical Psychologist</p>
    </div>
  </section>

  <section class="card card--back" aria-label="Card back">
    <svg class="tab tab--top" style="left:90px" viewBox="0 0 26 12"><polygon points="0,0 26,0 20,12 6,12" fill="var(--tab)"/></svg>
    <svg class="tab tab--bottom" style="left:380px" viewBox="0 0 26 12"><polygon points="6,0 20,0 26,12 0,12" fill="var(--tab)"/></svg>

    <div class="contact">
      <div class="contact__row">
        <svg class="contact__icon" viewBox="0 0 12 12"><circle cx="6" cy="6" r="5.2" fill="none" stroke="var(--navy)" stroke-width="1.2"/><circle cx="6" cy="5.2" r="1.8" fill="var(--navy)"/></svg>
        <div class="contact__address"><span>240 W. Lakeview Suite 310</span><span>Chicago, Illinois 60610</span></div>
      </div>
      <div class="contact__row">
        <svg class="contact__icon" viewBox="0 0 12 12"><circle cx="6" cy="6" r="5.2" fill="none" stroke="var(--navy)" stroke-width="1.2"/><path d="M4 3.5 L5.2 3.5 L5.6 5 L4.9 5.6 Q5.6 7 6.9 7.4 L7.5 6.7 L9 7.1 L9 8.3 Q5.5 8.6 4 3.5Z" fill="var(--navy)"/></svg>
        <span>312-555-0148</span>
      </div>
      <div class="contact__row">
        <svg class="contact__icon" viewBox="0 0 12 12"><circle cx="6" cy="6" r="5.2" fill="none" stroke="var(--navy)" stroke-width="1.2"/><rect x="3.2" y="4" width="5.6" height="4" fill="none" stroke="var(--navy)" stroke-width=".9"/><path d="M3.2 4 L6 6.2 L8.8 4" fill="none" stroke="var(--navy)" stroke-width=".9"/></svg>
        <span>drdanawhitfield@mailbox.com</span>
      </div>
    </div>

    <div class="identity">
      <span class="identity__mark"></span>
      <h2 class="identity__name">Dana Whitfield, Ph.D.</h2>
      <p class="identity__title">Licensed Clinical Psychologist</p>
    </div>
  </section>

</main>
</body>
</html>
```